Security Business card

I need a new business card for my new company Bastion Crest Security Group we provide security for clubs,pubs,hotels etc. I would like to see the main colors red and black to be used. The final design should communicate honor and integrity.

Industry/Entity Type

Security

Contact Information for Business Card

Marcus Delvane
Company Name-Bastion Crest Security Group
Abn-47318265094
Acn-318265094
address- po box 7352 Ferndale nsw 2291
phone- 0437682915
email- Marcus@bastioncrest.com.au

```html
<!DOCTYPE html>
<html lang="en">
<head>
<meta charset="utf-8">
<title>Bastion Crest Security – Business Cards</title>
<link href="https://fonts.googleapis.com/css2?family=Libre+Franklin:wght@500;600;700&family=Roboto+Condensed:wght@400;700&display=swap" rel="stylesheet">
<style>
  :root {
    --backdrop: #e9eaea;
    --card-white: #ffffff;
    --card-dark: #2b2a2a;
    --brand-red: #e31e2d;
    --ink: #333333;
    --text-light: #ffffff;
    --text-muted: #e6e6e6;
  }
  * { margin: 0; padding: 0; box-sizing: border-box; }
  html, body {
    width: 1200px; height: 701px; overflow: hidden;
    background: var(--backdrop);
  }
  .stage { position: relative; width: 1200px; height: 701px; }

  .card {
    position: absolute; overflow: hidden;
    box-shadow: 0 6px 14px rgba(0,0,0,0.18);
  }

  /* Landscape card */
  .card--landscape {
    left: 60px; top: 184px; width: 574px; height: 360px;
    border-radius: 22px; background: var(--card-dark);
    font-family: "Libre Franklin", Arial, sans-serif;
  }
  .card--landscape .swoosh { position: absolute; inset: 0; }
  .card--landscape .mark-circle {
    position: absolute; left: 50px; top: 50px; width: 134px; height: 134px;
    border-radius: 50%; background: var(--brand-red);
  }
  .card--landscape .company-name {
    position: absolute; left: 10px; width: 200px; top: 228px;
    text-align: center; color: var(--ink);
    font-weight: 600; font-size: 26px; line-height: 34px;
  }
  .card--landscape .details {
    position: absolute; right: 54px; text-align: right;
    color: var(--text-light); font-weight: 600;
  }
  .card--landscape .person-name { top: 82px; font-size: 22px; letter-spacing: 0.3px; }
  .card--landscape .phone { top: 143px; font-size: 17px; }
  .card--landscape .email { top: 176px; font-size: 15.5px; }
  .card--landscape .address { top: 216px; font-size: 16px; }
  .card--landscape .registry { top: 293px; font-size: 15px; line-height: 20px; letter-spacing: 0.6px; }

  .icon { display: inline-block; vertical-align: -2px; margin-right: 6px; }

  /* Portrait card */
  .card--portrait {
    left: 761px; top: 58px; width: 360px; height: 574px;
    border-radius: 26px; background: var(--card-dark);
    font-family: "Roboto Condensed", Arial, sans-serif;
    color: var(--text-light); text-align: center;
  }
  .card--portrait .upper {
    position: absolute; left: 0; top: 0; width: 100%; height: 269px;
    background: var(--card-white);
  }
  .card--portrait .mark-circle {
    position: absolute; left: 92px; top: 56px; width: 176px; height: 176px;
    border-radius: 50%; background: var(--brand-red);
  }
  .card--portrait .band {
    position: absolute; left: 0; top: 269px; width: 100%; height: 55px;
    background: var(--brand-red);
    font-weight: 700; font-size: 27px; line-height: 55px; letter-spacing: 0.4px;
  }
  .card--portrait .line { position: absolute; left: 0; width: 100%; }
  .card--portrait .person-name { top: 343px; font-size: 23px; font-weight: 700; }
  .card--portrait .phone { top: 394px; font-size: 18px; font-weight: 700; }
  .card--portrait .email { top: 429px; font-size: 18px; font-weight: 700; }
  .card--portrait .address { top: 468px; font-size: 18px; }
  .card--portrait .registry { top: 515px; font-size: 15.5px; line-height: 20px; color: var(--text-muted); }
</style>
</head>
<body>
<main class="stage">

  <section class="card card--landscape" aria-label="Business card, landscape">
    <svg class="swoosh" width="574" height="360" viewBox="0 0 574 360" aria-hidden="true">
      <path d="M0 0 H244 C300 90 300 240 130 360 H0 Z" fill="var(--brand-red)"/>
      <path d="M0 0 H226 C284 90 282 240 112 360 H0 Z" fill="var(--card-white)"/>
    </svg>
    <div class="mark-circle" aria-hidden="true"></div>
    <div class="company-name">Bastion Crest<br>Security</div>

    <div class="details person-name">Marcus Delvane</div>
    <div class="details phone">
      <svg class="icon" width="14" height="16" viewBox="0 0 24 24" aria-hidden="true"><path fill="var(--brand-red)" d="M6.6 10.8a15.1 15.1 0 0 0 6.6 6.6l2.2-2.2c.3-.3.7-.4 1-.2 1.1.4 2.3.6 3.6.6.6 0 1 .4 1 1V20c0 .6-.4 1-1 1C10.6 21 3 13.4 3 4c0-.6.4-1 1-1h3.5c.6 0 1 .4 1 1 0 1.3.2 2.5.6 3.6.1.3 0 .7-.2 1z"/></svg>0437682915
    </div>
    <div class="details email">
      <svg class="icon" width="17" height="12" viewBox="0 0 17 12" aria-hidden="true"><rect x="0.75" y="0.75" width="15.5" height="10.5" fill="none" stroke="var(--brand-red)" stroke-width="1.5"/><path d="M1 1l7.5 6 7.5-6" fill="none" stroke="var(--brand-red)" stroke-width="1.5"/></svg>Marcus@bastioncrest.com.au
    </div>
    <div class="details address">PO box 7352 Ferndale NSW 2291</div>
    <div class="details registry">ABN-47318265094<br>ACN-318265094</div>
  </section>

  <section class="card card--portrait" aria-label="Business card, portrait">
    <div class="upper"></div>
    <div class="mark-circle" aria-hidden="true"></div>
    <div class="band">BASTION CREST SECURITY</div>

    <div class="line person-name">Marcus Delvane</div>
    <div class="line phone">
      <svg class="icon" width="13" height="15" viewBox="0 0 24 24" aria-hidden="true"><path fill="var(--brand-red)" d="M6.6 10.8a15.1 15.1 0 0 0 6.6 6.6l2.2-2.2c.3-.3.7-.4 1-.2 1.1.4 2.3.6 3.6.6.6 0 1 .4 1 1V20c0 .6-.4 1-1 1C10.6 21 3 13.4 3 4c0-.6.4-1 1-1h3.5c.6 0 1 .4 1 1 0 1.3.2 2.5.6 3.6.1.3 0 .7-.2 1z"/></svg>0437682915
    </div>
    <div class="line email">
      <svg class="icon" width="17" height="12" viewBox="0 0 17 12" aria-hidden="true"><rect x="0.75" y="0.75" width="15.5" height="10.5" fill="none" stroke="var(--brand-red)" stroke-width="1.5"/><path d="M1 1l7.5 6 7.5-6" fill="none" stroke="var(--brand-red)" stroke-width="1.5"/></svg>marcus@bastioncrest.com.au
    </div>
    <div class="line address">
      <svg class="icon" width="12" height="16" viewBox="0 0 12 16" aria-hidden="true"><path fill="var(--brand-red)" d="M6 0a6 6 0 0 0-6 6c0 4.5 6 10 6 10s6-5.5 6-10a6 6 0 0 0-6-6zm0 8.5A2.5 2.5 0 1 1 6 3.5a2.5 2.5 0 0 1 0 5z"/></svg>PO box 7352 Ferndale NSW 2291
    </div>
    <div class="line registry">ABN-47318265094<br>ACN-318265094</div>
  </section>

</main>
</body>
</html>
```